Infection control

to re-design website to include the benefits of powdered bleach packed in pre-measured sachets which when dissolved in water provides economy, efficacy and is safe to use with the use of costly packaging. We need new text outlining the benefits of the world's most commonly used disinfectant for major hospitals, institutions, pathology, military and disaster areas.

Translate design into coded website using CMS with the following features:
Mobile responsive using HTML 5/ CSS3 standards
Coded with SEO standards and with H1 tags for easy spidering and with Wordpress CMS with is page rank 9
Site migration
Email support
Updates

Target Market(s)

hospitals, institutions, pathology, military and disaster areas

Industry/Entity Type

Chemical Product

Number of Pages Required

4 page

Colors

Designer to choose colors to be used in the design.

Requirements
Must have
• factual information based on the efficiency of sodium hypochlorite (bleach) used for infection control. The many viruses, bacteria, pathogens etc which certain strengths of bleach eliminate upon contact.
• As tis is a redesign, existing pages including MSDS sheets to stay the same
Nice to have
• a new look and feel including current logos
Should not have
• incorrect info

```html
<!DOCTYPE html>
<html lang="en">
<head>
<meta charset="utf-8">
<title>Clorava – Infection Control Website Pages</title>
<link rel="stylesheet" href="https://fonts.googleapis.com/css2?family=Montserrat:wght@400;700&family=Open+Sans:wght@400;600;700&display=swap">
<style>
:root{
  --stage:#2f4b6c;
  --blue:#2f7fb8;
  --blue-dark:#23669a;
  --blue-light:#dce9f3;
  --paper:#ffffff;
  --ink:#3b4147;
  --muted:#8a949c;
  --teal:#4d9fc6;
  --orange:#ef7a23;
  --green:#8cc63f;
  --dark:#2a2f34;
  --dark-2:#3a4148;
}
*{box-sizing:border-box;margin:0;padding:0}
html,body{width:1200px;height:935px;overflow:hidden}
body{background:var(--stage);font-family:"Open Sans",Arial,sans-serif;color:var(--ink);font-size:7px;line-height:1.45}
.board{display:flex;gap:20px;padding:22px 40px;height:935px;align-items:flex-start}
.page{width:360px;background:var(--paper);display:flex;flex-direction:column;box-shadow:0 6px 20px rgba(0,0,0,.3)}
.img{display:block}
h2,h3,.display{font-family:"Montserrat",Arial,sans-serif}
.btn{display:inline-block;background:var(--orange);color:#fff;font-size:6px;font-weight:700;padding:3px 8px;text-transform:uppercase}
.btn-green{background:var(--green);color:#fff;font-family:"Montserrat",Arial,sans-serif;font-weight:700;font-size:10px;padding:7px 16px;border-radius:14px;display:inline-flex;align-items:center;gap:8px}
.btn-green .arrow{width:16px;height:16px;border-radius:50%;background:#fff;color:var(--green);display:flex;align-items:center;justify-content:center;font-size:10px}

/* video band */
.video-band{position:relative;background:linear-gradient(180deg,#4a545c,#2a3036);display:flex;flex-direction:column;align-items:center;justify-content:center;color:#fff}
.play{width:26px;height:26px;border-radius:50%;border:2px solid #fff;display:flex;align-items:center;justify-content:center;margin-bottom:5px}
.video-band small{font-size:6px;letter-spacing:.08em;text-transform:uppercase}

/* about */
.about{display:flex}
.about-side{width:38%;background:var(--blue);color:#fff;padding:10px 10px}
.about-side h3{font-size:8px;text-transform:uppercase;margin-bottom:10px}
.feature{display:flex;gap:6px;margin-bottom:14px}
.feature .icon{flex:0 0 16px;height:16px;background:var(--green);display:flex;align-items:center;justify-content:center}
.feature b{display:block;color:var(--orange);font-size:7px}
.feature p{font-size:5.5px;opacity:.9}
.about-main{flex:1;padding:12px 12px;display:flex;flex-direction:column;gap:10px}
.product{display:flex;gap:8px;align-items:center}
.product-label{border:1px solid #ccd;padding:5px;flex:1}
.product-label .name{font-family:"Montserrat",Arial,sans-serif;font-weight:700;font-size:15px;color:var(--dark);line-height:1}
.product-label p{font-size:5px;color:var(--muted)}
.meter{font-size:5.5px;color:var(--muted)}
.meter .track{height:3px;background:#e4e8eb;margin-top:2px}
.meter .fill{height:3px;background:var(--orange)}

/* counters */
.counters{background:linear-gradient(180deg,#2b3237,#1f2428);color:#fff;padding:14px 18px 10px}
.counter-row{display:flex;justify-content:space-between;margin-bottom:8px}
.counter b{font-family:"Montserrat",Arial,sans-serif;font-size:12px;display:block}
.counter span{font-size:5px;color:#aab}
.call{font-family:"Montserrat",Arial,sans-serif;font-size:19px;letter-spacing:.02em}

/* blue list sections */
.split{display:flex}
.split .col-blue{background:var(--blue);color:#fff;padding:12px 10px;flex:1}
.split .col-light{background:var(--blue-light);padding:12px 10px;flex:1;display:flex;flex-direction:column;gap:8px}
.contact-line{display:flex;gap:5px;align-items:center;font-size:6px;margin-bottom:7px}
.contact-line .icon{width:14px;height:14px;background:var(--blue);display:flex;align-items:center;justify-content:center}
.list{list-style:none;font-size:6.5px;line-height:1.7}
.circle-photo{width:100px;height:100px;border-radius:50%;border:4px solid #fff;align-self:center}
.lead{font-size:7.5px;line-height:1.6}

/* centre page */
.site-header{height:40px;display:flex;align-items:center;justify-content:space-between;padding:0 12px;border-bottom:1px solid #eee}
.brand{display:flex;align-items:center;gap:4px;font-family:"Montserrat",Arial,sans-serif;font-weight:700;font-size:14px;color:var(--green)}
.brand .dot{width:12px;height:12px;border-radius:50%;background:var(--green)}
.nav{display:flex;gap:9px;font-size:5.5px;text-transform:uppercase;color:var(--muted)}
.nav .active{color:var(--orange)}
.hero{position:relative;height:160px}
.hero .img{position:absolute;inset:0}
.hero-text{position:absolute;left:0;right:0;top:62px;text-align:center;color:#fff;font-family:"Montserrat",Arial,sans-serif;font-weight:700;font-size:15px;text-shadow:0 1px 3px rgba(0,0,0,.4)}
.hero .btn{position:absolute;left:110px;top:90px}
.hero-phone{position:absolute;right:14px;bottom:14px;color:#fff;font-family:"Montserrat",Arial,sans-serif;font-size:12px}
.intro{padding:12px 20px;display:flex;flex-direction:column;gap:6px}
.intro h2{color:var(--teal);font-size:9px;text-align:center;font-weight:400;line-height:1.35;padding:0 20px}
.intro-body{display:flex;gap:10px}
.intro-body p{flex:1;font-size:5.5px;color:var(--muted)}
.intro h4{font-size:6px;color:var(--blue-dark);text-transform:uppercase}
.services{padding:4px 20px 10px}
.services h3{font-size:7px;color:var(--blue-dark);text-transform:uppercase;border-bottom:2px solid var(--orange);display:inline-block;margin-bottom:6px}
.services-row{display:flex;gap:10px}
.services-row p{font-size:5.5px;color:var(--muted);flex:1}
.service-icons{display:flex;justify-content:space-around;margin-top:8px}
.service-icons div{text-align:center;font-size:5px;color:var(--muted)}
.service-icons i{display:block;width:20px;height:20px;border-radius:50%;margin:0 auto 2px}

/* right page */
.testimonial{display:flex;gap:8px;align-items:center;margin-top:6px}
.contact{display:flex;background:var(--blue-light)}
.form{flex:1;background:var(--blue);padding:12px;display:flex;flex-direction:column;gap:6px;color:#fff}
.form h3{font-size:7px;text-transform:uppercase}
.field{height:12px;background:#fff}
.field.tall{height:30px}
.site-footer{background:var(--dark);color:#9aa;padding:10px 12px;display:flex;gap:12px;align-items:flex-start;font-size:5px}
.site-footer .col{flex:1;line-height:1.6}
.site-footer b{color:#fff;display:block;font-size:6px}
</style>
</head>
<body>
<main class="board">

  <!-- Page: About & product -->
  <section class="page" style="height:890px">
    <div class="video-band" style="height:170px">
      <div class="play"><svg width="10" height="10" viewBox="0 0 10 10"><path d="M2 1 L9 5 L2 9 Z" fill="#fff"/></svg></div>
      <small>Watch our product video</small>
    </div>
    <div class="about" style="height:300px">
      <div class="about-side">
        <h3>About</h3>
        <div class="feature"><span class="icon"><svg width="9" height="9" viewBox="0 0 10 10"><path d="M1 5 L4 8 L9 2" stroke="#fff" stroke-width="1.6" fill="none"/></svg></span><div><b>Safe</b><p>Simple sachets dissolve in water for a safe and measured solution every time.</p></div></div>
        <div class="feature"><span class="icon"><svg width="9" height="9" viewBox="0 0 10 10"><path d="M1 5 L4 8 L9 2" stroke="#fff" stroke-width="1.6" fill="none"/></svg></span><div><b>Economical</b><p>Pre-measured powder removes waste and cuts the cost of bulky packaging.</p></div></div>
        <div class="feature"><span class="icon"><svg width="9" height="9" viewBox="0 0 10 10"><path d="M1 5 L4 8 L9 2" stroke="#fff" stroke-width="1.6" fill="none"/></svg></span><div><b>Effective</b><p>Kills a wide range of viruses, bacteria and pathogens on contact.</p></div></div>
      </div>
      <div class="about-main">
        <div class="product">
          <svg class="img" role="img" aria-label="Photo of sachet product box" width="60" height="80"><rect width="60" height="80" fill="#e8ecef"/></svg>
          <div class="product-label"><div class="name">Chlor 5000</div><p>Powdered sodium hypochlorite sachets for hospital grade disinfection.</p></div>
        </div>
        <div class="meter">Viruses<div class="track"><div class="fill" style="width:92%"></div></div></div>
        <div class="meter">Bacteria<div class="track"><div class="fill" style="width:88%"></div></div></div>
        <div class="meter">Fungi<div class="track"><div class="fill" style="width:80%"></div></div></div>
        <div style="text-align:right;margin-top:auto"><span class="btn-green">Give feedback <span class="arrow">›</span></span></div>
      </div>
    </div>
    <div class="counters" style="height:120px">
      <div class="counter-row">
        <div class="counter"><b>561</b><span>Hospitals</span></div>
        <div class="counter"><b>25</b><span>Countries</span></div>
        <div class="counter"><b>236</b><span>Clinics</span></div>
        <div class="counter"><b>865</b><span>Clients</span></div>
      </div>
      <div class="call">CALL 1300 555 018</div>
    </div>
    <div class="split" style="height:300px">
      <div class="col-light" style="background:#fff">
        <div class="contact-line"><span class="icon"><svg width="8" height="8" viewBox="0 0 10 10"><path d="M2 1 L4 1 L5 3 L4 4 Q5 6 6 6 L7 5 L9 6 L9 8 Q5 9 1 3 Z" fill="#fff"/></svg></span>Call for orders</div>
        <div class="contact-line"><span class="icon"><svg width="8" height="8" viewBox="0 0 10 10"><path d="M5 1 A3 3 0 0 1 8 4 Q8 6 5 9 Q2 6 2 4 A3 3 0 0 1 5 1 Z" fill="#fff"/></svg></span>Find a stockist</div>
        <b style="font-size:7px;color:var(--blue-dark)">Pathology</b>
        <svg class="img circle-photo" role="img" aria-label="Photo of hospital cleaning staff" width="100" height="100"><circle cx="50" cy="50" r="50" fill="#7fa9c4"/></svg>
      </div>
      <div class="col-blue">
        <p class="lead">Our sachet is recommended for areas that have a high risk of exposure and infection. It is recommended for surfaces in wards, theatres and clinics under clean conditions.</p>
        <ul class="list" style="margin-top:10px">
          <li>Infectious Wards</li><li>Wiping tables and bench tops</li><li>Mopping floors</li><li>Sanitising treatment rooms</li><li>Disinfecting cutlery and linen</li><li>Operating theatres</li><li>Bench tops and floors</li>
        </ul>
      </div>
    </div>
  </section>

  <!-- Page: Home -->
  <section class="page" style="height:890px">
    <header class="site-header">
      <div class="brand"><span class="dot"></span>Clorava</div>
      <nav class="nav"><span class="active">Home</span><span>About</span><span>Products</span><span>MSDS</span><span>Contact</span></nav>
    </header>
    <div class="hero">
      <svg class="img" role="img" aria-label="Photo of laboratory glassware through a diamond fence" width="360" height="160"><defs><linearGradient id="heroG" x1="0" y1="0" x2="1" y2="1"><stop offset="0" stop-color="#c9d6df"/><stop offset="1" stop-color="#6f8fa6"/></linearGradient></defs><rect width="360" height="160" fill="url(#heroG)"/></svg>
      <div class="hero-text">100% Australian owned and operated</div>
      <span class="btn">Read more</span>
      <div class="hero-phone">1300 555 018</div>
    </div>
    <div class="intro" style="height:200px">
      <h2>Our values are based on supplying quality products on time distribution and benefits to the user</h2>
      <div class="intro-body">
        <p>Sodium hypochlorite is the most widely used disinfectant in the world. Our pre-measured powdered sachets give hospitals, institutions, pathology units, military forces and disaster teams a reliable solution that is easy to store, easy to carry and simple to prepare. One sachet in the stated volume of water delivers the right strength every time, with no guesswork and far less packaging. It is proven against bacteria, viruses, fungi and spores when used as directed.<br><br><span class="intro h4" style="color:var(--blue-dark);font-weight:700">UPDATE ON USE IN HEALTH CARE FACILITIES</span><br>Guidance on dilution rates, contact times and storage is available for every site, with full safety data sheets provided for staff.</p>
        <svg class="img" role="img" aria-label="Photo of dispenser bottle" width="70" height="120"><rect width="70" height="120" fill="#f1f3f5"/></svg>
      </div>
      <div><span class="btn">Read more</span></div>
    </div>
    <div class="services" style="height:130px">
      <h3>Our Services</h3>
      <div class="services-row">
        <svg class="img" role="img" aria-label="Illustration of medical service icons" width="120" height="55"><rect width="120" height="55" fill="#9cc3dc"/></svg>
        <p>We supply and deliver across the country, support training for cleaning staff and provide clear advice on safe handling for every facility we serve.</p>
      </div>
      <div class="service-icons">
        <div><i style="background:#e0463a"></i>Supply and delivery</div>
        <div><i style="background:var(--blue)"></i>Staff training</div>
        <div><i style="background:#2aa99a"></i>Safety data</div>
      </div>
    </div>
    <div class="video-band" style="height:100px">
      <div class="play"><svg width="10" height="10" viewBox="0 0 10 10"><path d="M2 1 L9 5 L2 9 Z" fill="#fff"/></svg></div>
      <small>Watch our product video</small>
    </div>
    <div class="about" style="height:270px">
      <div class="about-side">
        <h3>About</h3>
        <div class="feature"><span class="icon"><svg width="9" height="9" viewBox="0 0 10 10"><path d="M1 5 L4 8 L9 2" stroke="#fff" stroke-width="1.6" fill="none"/></svg></span><div><b>Safe</b><p>Measured sachets for a safe solution.</p></div></div>
        <div class="feature"><span class="icon"><svg width="9" height="9" viewBox="0 0 10 10"><path d="M1 5 L4 8 L9 2" stroke="#fff" stroke-width="1.6" fill="none"/></svg></span><div><b>Economical</b><p>Less waste and lower freight costs.</p></div></div>
        <div class="feature"><span class="icon"><svg width="9" height="9" viewBox="0 0 10 10"><path d="M1 5 L4 8 L9 2" stroke="#fff" stroke-width="1.6" fill="none"/></svg></span><div><b>Effective</b><p>Acts fast against common pathogens.</p></div></div>
      </div>
      <div class="about-main">
        <div class="product">
          <svg class="img" role="img" aria-label="Photo of sachet product box" width="50" height="70"><rect width="50" height="70" fill="#e8ecef"/></svg>
          <div class="product-label"><div class="name">Chlor 5000</div><p>Powdered sodium hypochlorite sachets.</p></div>
        </div>
        <div class="meter">Viruses<div class="track"><div class="fill" style="width:92%"></div></div></div>
        <div class="meter">Bacteria<div class="track"><div class="fill" style="width:88%"></div></div></div>
        <div class="meter">Fungi<div class="track"><div class="fill" style="width:80%"></div></div></div>
        <div style="text-align:right;margin-top:auto"><span class="btn-green">Give feedback <span class="arrow">›</span></span></div>
      </div>
    </div>
  </section>

  <!-- Page: Uses & contact -->
  <section class="page" style="height:860px;margin-top:20px">
    <div class="split" style="height:420px">
      <div class="col-light" style="background:#fff">
        <b style="font-size:7px;color:var(--blue-dark)">Radiology</b>
        <svg class="img circle-photo" role="img" aria-label="Photo of nurse in hospital corridor" width="100" height="100"><circle cx="50" cy="50" r="50" fill="#86aec8"/></svg>
        <span class="btn" style="align-self:flex-start">Read more</span>
        <div style="background:var(--blue);color:#fff;padding:8px;margin-top:6px">
          <b style="font-size:7px">Get our sachets</b>
          <div class="meter" style="color:#dce">Stock level<div class="track"><div class="fill" style="width:70%"></div></div></div>
          <div class="meter" style="color:#dce">Orders met<div class="track"><div class="fill" style="width:85%"></div></div></div>
        </div>
        <b style="font-size:7px;color:var(--blue-dark);margin-top:4px">What our clients say</b>
        <div class="testimonial">
          <svg class="img" role="img" aria-label="Photo of clean hospital ward" width="70" height="70"><circle cx="35" cy="35" r="35" fill="#9bb8cc"/></svg>
          <p style="font-size:5.5px;color:var(--muted);flex:1">Easy to store and quick to prepare for our ward teams.</p>
        </div>
      </div>
      <div class="col-blue">
        <ul class="list">
          <li>Infectious Wards</li><li>Wiping tables and bench tops</li><li>Mopping floors</li><li>Sanitising treatment rooms</li><li>Disinfecting cutlery and linen</li><li>Implements used by patients</li><li>Operating theatres</li><li>Mopping floors</li><li>Bench tops and floors</li>
        </ul>
        <p class="lead" style="margin-top:10px">Our sachet is recommended for areas that carry a high risk of exposure and infection. It has been assessed for hospital grade disinfection under clean conditions.</p>
        <p class="lead" style="margin-top:8px">Theatre<br>Blood and body fluids</p>
        <p class="lead" style="margin-top:8px">Radiology and laboratories<br>Wash and rinse instruments, then soak in fresh solution.</p>
      </div>
    </div>
    <div class="counters" style="height:90px;display:flex;align-items:center;justify-content:center">
      <div class="call">CALL 1300 555 018</div>
    </div>
    <div class="contact" style="height:250px">
      <div class="form">
        <h3>Contact us</h3>
        <div class="field"></div><div class="field"></div><div class="field"></div><div class="field tall"></div>
        <span class="btn" style="align-self:flex-start">Send</span>
      </div>
      <svg class="img" role="img" aria-label="Map showing office location" width="170" height="250"><rect width="170" height="250" fill="#e4e7ea"/></svg>
    </div>
    <footer class="site-footer" style="height:100px">
      <div class="col"><div class="brand" style="font-size:12px"><span class="dot"></span>Clorava</div></div>
      <div class="col"><b>Products</b>Sachets<br>Safety data<br>Orders</div>
      <div class="col"><b>Company</b>About us<br>Services<br>Contact</div>
      <div class="col"><b>Call</b>1300 555 018</div>
    </footer>
  </section>

</main>
</body>
</html>
```